Yard Sign Design for luxury design & build company

Looking to have 18" x 24" company yard signs designed.
An update to the business logo might be helpful.
Photos are not necessary but use if you can make inspiring.

Industry: Construction

Looking for a large headline of "Basement Finishing"
Website: www.lumenfieldhomes.com
Phone Number (612) 555-0147
FB link: facebook.com/lumenfieldhomesmn
Instagram: www.instagram.com/lumenfieldhomesmn

Industry/Entity Type

Construction

Colors

Designer to choose colors to be used in the design.

Requirements
Must have
• Impactful high end characteristics
Nice to have
• Depth and detail graphis

```html
<!DOCTYPE html>
<html lang="en">
<head>
<meta charset="utf-8">
<title>Lumenfield Homes – Basement Finishing Yard Sign</title>
<link href="https://fonts.googleapis.com/css2?family=Anton&family=Montserrat:wght@600;700;800&display=swap" rel="stylesheet">
<style>
  :root {
    --red: #d8232a;
    --black: #111111;
    --white: #ffffff;
    --page: #e9e9e9;
    --badge: #f2f2f2;
    --muted: #cfcfcf;
  }
  * { box-sizing: border-box; margin: 0; padding: 0; }
  html, body {
    width: 1200px;
    height: 2400px;
    overflow: hidden;
    background: var(--page);
  }
  .sign {
    position: absolute;
    left: 40px;
    top: 780px;
    width: 1120px;
    height: 840px;
    background: var(--white);
    overflow: hidden;
    box-shadow: 0 6px 24px rgba(0,0,0,.15);
  }
  .sign-shapes {
    position: absolute;
    inset: 0;
  }
  .brand {
    position: absolute;
    top: 62px;
    left: 0;
    width: 100%;
    display: flex;
    justify-content: center;
    align-items: center;
    gap: 20px;
  }
  .brand-dot {
    width: 62px;
    height: 62px;
    border-radius: 50%;
    background: var(--red);
  }
  .brand-name {
    font-family: "Montserrat", sans-serif;
    font-weight: 800;
    font-size: 50px;
    letter-spacing: 3px;
    color: var(--black);
  }
  .headline {
    position: absolute;
    left: 0;
    width: 100%;
    text-align: center;
    font-family: "Anton", sans-serif;
    font-size: 138px;
    line-height: 1;
    letter-spacing: 2px;
    text-transform: uppercase;
  }
  .headline-top { top: 262px; color: var(--white); }
  .headline-bottom { top: 398px; color: var(--red); }
  .phone-band {
    position: absolute;
    left: 0;
    top: 560px;
    width: 100%;
    height: 96px;
    background: var(--red);
    display: flex;
    justify-content: center;
    align-items: center;
    gap: 22px;
  }
  .phone-icon { width: 64px; height: 64px; }
  .phone-number {
    font-family: "Montserrat", sans-serif;
    font-weight: 800;
    font-size: 72px;
    color: var(--white);
    letter-spacing: 1px;
  }
  .footer {
    position: absolute;
    left: 0;
    top: 656px;
    width: 100%;
    height: 184px;
    background: var(--black);
  }
  .review-badge {
    position: absolute;
    left: 48px;
    top: 46px;
    width: 180px;
    height: 92px;
    border-radius: 10px;
    background: var(--badge);
  }
  .contact {
    position: absolute;
    left: 270px;
    right: 40px;
    top: 36px;
    text-align: center;
    font-family: "Montserrat", sans-serif;
    color: var(--white);
  }
  .website {
    font-weight: 800;
    font-size: 52px;
    letter-spacing: 1px;
  }
  .social {
    margin-top: 22px;
    display: flex;
    justify-content: center;
    align-items: center;
    gap: 16px;
  }
  .social-label {
    font-weight: 600;
    font-size: 20px;
    letter-spacing: 2px;
    color: var(--muted);
  }
  .social-dot {
    width: 30px;
    height: 30px;
    border-radius: 50%;
    background: var(--red);
  }
  .social-handle {
    font-weight: 700;
    font-size: 36px;
  }
</style>
</head>
<body>
  <main class="sign">
    <svg class="sign-shapes" width="1120" height="840" viewBox="0 0 1120 840" aria-hidden="true">
      <path d="M0 250 Q 520 150 1120 205 L1120 840 L0 840 Z" fill="var(--red)"/>
      <path d="M0 278 Q 540 178 1120 232 L1120 840 L0 840 Z" fill="var(--black)"/>
    </svg>

    <div class="brand">
      <span class="brand-dot"></span>
      <span class="brand-name">LUMENFIELD HOMES</span>
    </div>

    <h1 class="headline headline-top">Basement</h1>
    <h2 class="headline headline-bottom">Finishing</h2>

    <div class="phone-band">
      <svg class="phone-icon" viewBox="0 0 64 64" aria-hidden="true">
        <circle cx="32" cy="32" r="30" fill="var(--white)"/>
        <path d="M22 16c2-1 4 0 5 2l3 6c1 2 0 4-1 5l-2 2c2 5 6 9 11 11l2-2c1-1 3-2 5-1l6 3c2 1 3 3 2 5l-2 4c-1 2-3 3-6 3C30 53 11 34 12 21c0-3 1-5 3-6z" fill="var(--red)"/>
      </svg>
      <span class="phone-number">(612) 555-0147</span>
    </div>

    <footer class="footer">
      <div class="review-badge"></div>
      <div class="contact">
        <div class="website">www.lumenfieldhomes.com</div>
        <div class="social">
          <span class="social-label">FOLLOW US ON</span>
          <span class="social-dot"></span>
          <span class="social-handle">@lumenfieldhomesmn</span>
        </div>
      </div>
    </footer>
  </main>
</body>
</html>
```